New cool to-go cup for KELMO Coffee

UPDATE MARCH 18: Please read the attached document "Design ideas - Front" with a mock-up of the design we are looking for. And please don't change the logo.

We are looking for a new cool design for our to-go cups in kraft paper (same style as the attached photo).

The idea:

We have three different cups sizes: 6oz, 8oz and 12oz. We call them “Tiny-Lark” (6oz), “Mid-Wren” (8oz) and “Tall-heron” (12oz) (refers to the size in milliliters). We would like to include this in the cup design. Please see the attached sketch of the idea ("Design ideas - Front").

The backside of the cup should have the attached text and logo ("Design ideas - Back").

But other ideas are also very welcome too! Maybe just a simple cup with the logo.

Please keep the design very minimalistic. The more simple the better.

Target Market(s)

Young urban people

Industry/Entity Type

Coffee shop

Font styles to use
Sans Serif

Requirements
Must have
• Kraft paper cups

```html
<!DOCTYPE html>
<html lang="en">
<head>
<meta charset="utf-8">
<title>KELMO Coffee – to-go cup range</title>
<link rel="stylesheet" href="https://fonts.googleapis.com/css2?family=Montserrat:wght@400;700&display=swap">
<style>
  :root {
    --paper: #ffffff;
    --divider: #c4c4c4;
    --kraft: #a2865f;
    --kraft-dark: #8c7049;
    --kraft-light: #b09670;
    --stripe: #9a7d55;
    --cup-white: #f2f2f2;
    --cup-shade: #dcdcdc;
    --lid-light: #fafafa;
    --lid-mid: #e4e4e4;
    --lid-dark: #c9c9c9;
    --ink: #1d130c;
    --hashtag: #141414;
  }
  * { margin: 0; padding: 0; box-sizing: border-box; }
  html, body { width: 825px; height: 1200px; overflow: hidden; background: var(--paper); }
  .cup-range { display: block; width: 825px; height: 1200px; }
  .divider { stroke: var(--divider); stroke-width: 1.5; }
  .cup-white { fill: var(--cup-white); }
  .cup-rim { fill: var(--cup-shade); }
  .lid { fill: url(#lid-sheen); }
  .lid-rim { fill: url(#rim-sheen); }
  .stripe { fill: var(--stripe); }
  .kraft-band { fill: url(#kraft-tone); }
  .size-tag { font-family: 'Montserrat', sans-serif; fill: var(--hashtag); text-anchor: middle; }
  .size-tag .strong { font-weight: 700; }
  .size-tag .light { font-weight: 400; }
  .brand-ring { fill: none; stroke: var(--ink); }
  .brand-name { font-family: 'Montserrat', sans-serif; font-weight: 700; fill: var(--ink); text-anchor: middle; letter-spacing: 0.12em; }
  .back-copy { font-family: 'Montserrat', sans-serif; font-weight: 400; fill: var(--ink); text-anchor: middle; }
</style>
</head>
<body>
<svg class="cup-range" viewBox="0 0 825 1200" xmlns="http://www.w3.org/2000/svg">
  <defs>
    <linearGradient id="lid-sheen" x1="0" x2="1" y1="0" y2="0">
      <stop offset="0" stop-color="var(--lid-dark)"/>
      <stop offset="0.35" stop-color="var(--lid-light)"/>
      <stop offset="0.7" stop-color="var(--lid-mid)"/>
      <stop offset="1" stop-color="var(--lid-dark)"/>
    </linearGradient>
    <linearGradient id="rim-sheen" x1="0" x2="1" y1="0" y2="0">
      <stop offset="0" stop-color="var(--lid-mid)"/>
      <stop offset="0.5" stop-color="var(--lid-light)"/>
      <stop offset="1" stop-color="var(--lid-mid)"/>
    </linearGradient>
    <linearGradient id="kraft-tone" x1="0" x2="1" y1="0" y2="0">
      <stop offset="0" stop-color="var(--kraft-dark)"/>
      <stop offset="0.45" stop-color="var(--kraft)"/>
      <stop offset="0.8" stop-color="var(--kraft-light)"/>
      <stop offset="1" stop-color="var(--kraft)"/>
    </linearGradient>

    <!-- Tiny-Lark cup -->
    <g id="cup-tiny">
      <path class="cup-white" d="M63 228 L255 228 L229 466 Q158 478 87 466 Z"/>
      <rect class="stripe" x="65" y="251" width="188" height="3"/>
      <path class="kraft-band" d="M66 259 L252 259 L232.7 455 L85.3 455 Z"/>
      <path class="lid" d="M78 178 Q158 170 238 178 L253 222 L65 222 Z"/>
      <rect class="lid-rim" x="54" y="222" width="210" height="12" rx="4"/>
    </g>

    <!-- Mid-Wren cup -->
    <g id="cup-mid">
      <path class="cup-white" d="M285 184 L492 184 L467 467 Q389 480 310 467 Z"/>
      <rect class="stripe" x="287" y="211" width="203" height="3.5"/>
      <rect class="stripe" x="288" y="219" width="201" height="2"/>
      <path class="kraft-band" d="M289 230 L488 230 L469.4 445 L307.6 445 Z"/>
      <path class="lid" d="M294 127 Q389 119 484 127 L494 177 L282 177 Z"/>
      <rect class="lid-rim" x="271" y="177" width="231" height="12" rx="4"/>
    </g>

    <!-- Tall-heron cup -->
    <g id="cup-tall">
      <path class="cup-white" d="M521 153 L742 153 L714 472 Q631 486 549 472 Z"/>
      <rect class="stripe" x="522" y="173" width="219" height="3.5"/>
      <rect class="stripe" x="523" y="189" width="217" height="3"/>
      <rect class="stripe" x="524" y="197" width="215" height="2"/>
      <path class="kraft-band" d="M525.6 207 L737.4 207 L716.3 452 L546.7 452 Z"/>
      <path class="lid" d="M526 92 Q631 84 734 92 L740 145 L515 145 Z"/>
      <rect class="lid-rim" x="507" y="145" width="244" height="12" rx="4"/>
    </g>
  </defs>

  <!-- Front row -->
  <g class="cup-front">
    <use href="#cup-tiny"/>
    <text class="size-tag" x="158" y="287" font-size="20"><tspan class="strong">#tiny</tspan><tspan class="light">lark</tspan></text>
    <circle class="brand-ring" cx="158" cy="355" r="50" stroke-width="2.5"/>
    <text class="brand-name" x="158" y="352" font-size="13">KELMO</text>
    <text class="brand-name" x="158" y="369" font-size="13">Coffee</text>

    <use href="#cup-mid"/>
    <text class="size-tag" x="389" y="262" font-size="21"><tspan class="strong">#mid</tspan><tspan class="light">wren</tspan></text>
    <circle class="brand-ring" cx="389" cy="337" r="57" stroke-width="2.8"/>
    <text class="brand-name" x="389" y="334" font-size="15">KELMO</text>
    <text class="brand-name" x="389" y="353" font-size="15">Coffee</text>

    <use href="#cup-tall"/>
    <text class="size-tag" x="631" y="241" font-size="22"><tspan class="strong">#tall</tspan><tspan class="light">heron</tspan></text>
    <circle class="brand-ring" cx="631" cy="322" r="65" stroke-width="3"/>
    <text class="brand-name" x="631" y="318" font-size="17">KELMO</text>
    <text class="brand-name" x="631" y="340" font-size="17">Coffee</text>
  </g>

  <line class="divider" x1="0" y1="600" x2="825" y2="600"/>

  <!-- Back row -->
  <g class="cup-back" transform="translate(0 600)">
    <use href="#cup-tiny"/>
    <circle class="brand-ring" cx="158" cy="323" r="16" stroke-width="1.2"/>
    <text class="brand-name" x="158" y="323" font-size="5.5">KELMO</text>
    <text class="brand-name" x="158" y="330" font-size="5.5">Coffee</text>
    <text class="back-copy" font-size="6">
      <tspan x="158" y="352">Read about your coffee</tspan>
      <tspan x="158" y="359">and the dedicated farmers</tspan>
      <tspan x="158" y="366">who made this cup possible:</tspan>
      <tspan x="158" y="380">www.kelmo.com</tspan>
      <tspan x="158" y="393">@kelmocom</tspan>
    </text>

    <use href="#cup-mid"/>
    <circle class="brand-ring" cx="389" cy="305" r="17" stroke-width="1.3"/>
    <text class="brand-name" x="389" y="305" font-size="6">KELMO</text>
    <text class="brand-name" x="389" y="312" font-size="6">Coffee</text>
    <text class="back-copy" font-size="6.6">
      <tspan x="389" y="338">Read about your coffee</tspan>
      <tspan x="389" y="346">and the dedicated farmers</tspan>
      <tspan x="389" y="354">who made this cup possible:</tspan>
      <tspan x="389" y="369">www.kelmo.com</tspan>
      <tspan x="389" y="385">@kelmocom</tspan>
    </text>

    <use href="#cup-tall"/>
    <circle class="brand-ring" cx="631" cy="284" r="20" stroke-width="1.5"/>
    <text class="brand-name" x="631" y="284" font-size="7">KELMO</text>
    <text class="brand-name" x="631" y="292" font-size="7">Coffee</text>
    <text class="back-copy" font-size="7.4">
      <tspan x="631" y="320">Read about your coffee</tspan>
      <tspan x="631" y="329">and the dedicated farmers</tspan>
      <tspan x="631" y="338">who made this cup possible:</tspan>
      <tspan x="631" y="355">www.kelmo.com</tspan>
      <tspan x="631" y="373">@kelmocom</tspan>
    </text>
  </g>
</svg>
</body>
</html>
```